Brochure and Logo design for nature connection support service

Brochure design for business supporting people with psycho-social disabilities to develop a connection with nature. We do bush walking, camping and bush-craft related activities to help people feel home in the outdoors. My vision is for more people to develop a transformative relationship with Nature creating more fulfilling, connected, and environmentally-sustainable communities. I have attached for inclusion some notes and a photo of myself.

I also need a logo. I have attached a sketch of a basic idea that I had incorporating a tree surrounding a sitting figure. The person, fire and tree could blend into each other and re-combine like an ouroborus (see attached image). I have also attached a circular image of melantor sitting which has nice proportions for a circular logo.

For inspo, some concepts that I resonate with are: mind, consciousness, psychedelic values, wonder, wisdom, philosophy, plants, ecology, ecosystems (esp. Australian woodlands), the night sky, ancient civilisations, primitive societies, minimalism, balance, dynamic equilibrium...

Target Market(s)

The brochure will be aimed at potential participants, so should be concise and appealing. It will also be directed to the carers and Support Coordinators of people with disabilities, so it should be professional, sincere, and not sales-pitchy.

Logo Text

"nature connection" "support services" Some combinations of symbols and text and symbol without text

Requirements
Must have
• 1 page double sided able to be folded in three.
Green colour scheme
Photo of myself should be associated with the "contact" section. Can be cropped to headshot if appropriate etc. Neither photo should be too prominent. Other images are okay.

```html
<!DOCTYPE html>
<html lang="en">
<head>
<meta charset="utf-8">
<title>Greenway Outdoor Support Services – Trifold Brochure</title>
<link href="https://fonts.googleapis.com/css2?family=Montserrat:wght@400;500;600;700;800&display=swap" rel="stylesheet">
<style>
  :root{
    --bg:#eef1ee;
    --paper:#ffffff;
    --green-deep:#1d6f2b;
    --green:#36a234;
    --green-mid:#5bb531;
    --green-light:#8cc63f;
    --forest-dark:#1f4d22;
    --forest:#3f8a3a;
    --ink:#2b2f2b;
    --ink-soft:#555b55;
  }
  *{box-sizing:border-box;margin:0;padding:0}
  html,body{width:1200px;height:2398px;overflow:hidden}
  body{background:var(--bg);font-family:"Montserrat",Arial,sans-serif;color:var(--ink);position:relative}

  .sheet{position:absolute;left:50px;width:1100px;height:850px;background:var(--paper);box-shadow:0 10px 30px rgba(0,0,0,.12);overflow:hidden}
  .sheet--outside{top:250px}
  .sheet--inside{top:1300px}
  .sheet__art{position:absolute;inset:0;width:1100px;height:850px}
  .fold{position:absolute;top:0;bottom:0;width:1px;background:rgba(0,0,0,.06)}

  .panel{position:absolute;top:0;height:850px;width:366px}
  .panel--left{left:0}
  .panel--middle{left:367px}
  .panel--right{left:734px}

  .heading{font-weight:800;text-transform:uppercase;line-height:1.1}
  .heading--light{color:#fff;font-size:19px}
  .heading--green{color:var(--green-deep);font-size:24px}
  .heading--green .accent{color:var(--green)}
  .heading-rule{display:block;width:60px;height:4px;background:var(--green-light);margin-top:8px;border-radius:2px}
  .copy{font-size:13px;line-height:1.55}
  .copy--light{color:#eaf6e4}
  .copy--dark{color:var(--ink-soft)}

  /* outside – left */
  .need{position:absolute;left:34px;top:48px;width:300px}
  .cost{position:absolute;left:34px;top:250px;width:300px}
  .need .copy,.cost .copy{margin-top:12px}

  /* outside – middle */
  .contact-title{position:absolute;left:0;width:366px;top:70px;text-align:center;color:#fff;font-weight:700;font-size:17px;letter-spacing:.5px}
  .contact{position:absolute;left:40px;top:430px;width:290px}
  .contact__name{font-size:24px;font-weight:700;color:var(--ink)}
  .contact__phone{display:inline-block;margin-top:8px;background:var(--green);color:#fff;font-weight:700;font-size:26px;padding:2px 12px;letter-spacing:1px}
  .contact__email{margin-top:8px;font-size:14px;font-weight:500;color:var(--ink)}
  .contact__bio{margin-top:18px}

  /* cover */
  .brand{position:absolute;left:40px;top:500px;width:290px;display:flex;align-items:center;gap:14px}
  .brand__dot{flex:0 0 54px;height:54px;border-radius:50%;background:var(--green)}
  .brand__name{font-weight:800;font-size:25px;line-height:1.08;color:var(--green-deep);text-transform:uppercase}

  /* inside – left */
  .does{position:absolute;left:34px;top:44px;width:300px}
  .does .copy{margin-top:14px}
  .benefits{position:absolute;left:30px;top:440px;width:310px;list-style:none}
  .benefit{display:flex;gap:14px;margin-bottom:28px;align-items:flex-start}
  .benefit__icon{flex:0 0 40px;height:40px}
  .benefit__title{font-weight:800;font-size:15px;color:var(--green-deep);text-transform:uppercase}
  .benefit__text{font-size:12.5px;line-height:1.45;color:var(--ink-soft);margin-top:3px}

  /* inside – middle */
  .what-is{position:absolute;left:30px;top:395px;width:305px}
  .what-is .copy{margin-top:12px}
  .ticks{list-style:none;margin:12px 0}
  .ticks li{font-size:13px;color:var(--ink-soft);padding-left:20px;position:relative;line-height:1.7}
  .ticks li::before{content:"";position:absolute;left:0;top:8px;width:9px;height:9px;background:var(--green);border-radius:2px}

  /* inside – right */
  .doing{position:absolute;left:30px;top:330px;width:305px}
  .where{position:absolute;left:30px;top:560px;width:305px}
  .doing .copy,.where .copy{margin-top:12px}
</style>
</head>
<body>

<!-- OUTSIDE OF SHEET -->
<section class="sheet sheet--outside" aria-label="Brochure outside">
  <svg class="sheet__art" viewBox="0 0 1100 850" aria-hidden="false">
    <defs>
      <linearGradient id="greenPanel" x1="0" y1="0" x2="0" y2="1">
        <stop offset="0" stop-color="#3ea737"/>
        <stop offset="1" stop-color="#1d6f2b"/>
      </linearGradient>
      <radialGradient id="forestTone" cx=".5" cy=".45" r=".65">
        <stop offset="0" stop-color="#4f9a45"/>
        <stop offset="1" stop-color="#1f4d22"/>
      </radialGradient>
      <radialGradient id="portraitTone" cx=".5" cy=".4" r=".6">
        <stop offset="0" stop-color="#d9cbb8"/>
        <stop offset="1" stop-color="#7d7a6b"/>
      </radialGradient>
    </defs>

    <!-- left panel -->
    <rect x="0" y="0" width="367" height="850" fill="url(#greenPanel)"/>
    <g role="img" aria-label="Line illustration of a large tropical leaf">
      <circle cx="90" cy="740" r="150" fill="#185f25"/>
      <circle cx="90" cy="740" r="150" fill="none" stroke="#ffffff" stroke-width="3"/>
    </g>

    <!-- middle panel -->
    <path d="M367 0 H734 V300 C650 350 480 360 367 320 Z" fill="url(#greenPanel)"/>
    <path d="M367 320 C480 360 650 350 734 300 V322 C650 372 480 382 367 342 Z" fill="#8cc63f"/>
    <g role="img" aria-label="Portrait photo of the support worker">
      <circle cx="550" cy="215" r="110" fill="#ffffff"/>
      <circle cx="550" cy="215" r="100" fill="url(#portraitTone)"/>
    </g>
    <path d="M367 850 V790 C480 760 620 800 734 760 V850 Z" fill="#36a234"/>

    <!-- right panel (cover) -->
    <path d="M734 0 H1100 V360 C1040 430 930 450 860 410 C790 370 760 280 734 220 Z" fill="#36a234"/>
    <g role="img" aria-label="Aerial photo of a winding road through dense forest">
      <path d="M760 0 H1100 V340 C1040 405 940 425 875 390 C810 355 785 270 760 200 Z" fill="url(#forestTone)"/>
    </g>
    <path d="M734 720 C850 690 980 740 1100 660 V850 H734 Z" fill="#36a234"/>
    <path d="M734 700 C850 670 980 715 1100 640 V660 C980 740 850 690 734 720 Z" fill="#8cc63f"/>
  </svg>
  <div class="fold" style="left:367px"></div>
  <div class="fold" style="left:734px"></div>

  <div class="panel panel--left">
    <div class="need">
      <h2 class="heading heading--light">What will I need?<span class="heading-rule"></span></h2>
      <p class="copy copy--light">Comfortable clothes, sturdy shoes, a water bottle and a small backpack. We can help with any extra gear you may need.</p>
    </div>
    <div class="cost">
      <h2 class="heading heading--light">What does it cost?<span class="heading-rule"></span></h2>
      <p class="copy copy--light">Sessions can be funded through your support plan under capacity building. Contact us to talk about pricing and options that suit you.</p>
    </div>
  </div>

  <div class="panel panel--middle">
    <h2 class="contact-title">WHO DO I CONTACT?</h2>
    <div class="contact">
      <p class="contact__name">Corin Ashdale</p>
      <p class="contact__phone">0491 570 110</p>
      <p class="contact__email">corin.ashdale@example.com</p>
      <p class="copy copy--dark contact__bio">Corin has a background in mental health support work, outdoor leadership and bushcraft, with study in ecological restoration, psychology and ecology.</p>
    </div>
  </div>

  <div class="panel panel--right">
    <div class="brand">
      <span class="brand__dot"></span>
      <p class="brand__name">Greenway Outdoor Support Services</p>
    </div>
  </div>
</section>

<!-- INSIDE OF SHEET -->
<section class="sheet sheet--inside" aria-label="Brochure inside">
  <svg class="sheet__art" viewBox="0 0 1100 850">
    <defs>
      <linearGradient id="greenTop" x1="0" y1="0" x2="1" y2="1">
        <stop offset="0" stop-color="#5bb531"/>
        <stop offset="1" stop-color="#2f8f2f"/>
      </linearGradient>
      <linearGradient id="bushTone" x1="0" y1="0" x2="1" y2="1">
        <stop offset="0" stop-color="#5c7a4a"/>
        <stop offset=".5" stop-color="#2f4f2c"/>
        <stop offset="1" stop-color="#6e5a40"/>
      </linearGradient>
    </defs>

    <!-- left panel green top -->
    <path d="M0 0 H367 V330 C280 390 120 400 0 360 Z" fill="url(#greenTop)"/>
    <path d="M0 360 C120 400 280 390 367 330 V352 C280 412 120 422 0 382 Z" fill="#8cc63f"/>

    <!-- photo across middle and right -->
    <g role="img" aria-label="Photo of a person walking along a trail in tall rainforest">
      <path d="M367 0 H1100 V170 C1000 240 860 270 720 270 C580 270 460 320 367 370 Z" fill="url(#bushTone)"/>
    </g>
    <path d="M367 370 C460 320 580 270 720 270 C860 270 1000 240 1100 170 V200 C1000 270 860 300 720 300 C580 300 460 350 367 400 Z" fill="#36a234"/>
    <path d="M367 400 C460 350 580 300 720 300 C860 300 1000 270 1100 200 V214 C1000 284 860 314 720 314 C580 314 460 364 367 414 Z" fill="#8cc63f"/>

    <!-- bottom swoosh -->
    <path d="M0 800 C300 760 700 830 1100 770 V850 H0 Z" fill="#36a234"/>
    <path d="M0 782 C300 742 700 812 1100 752 V770 C700 830 300 760 0 800 Z" fill="#8cc63f"/>
  </svg>
  <div class="fold" style="left:367px"></div>
  <div class="fold" style="left:734px"></div>

  <div class="panel panel--left">
    <div class="does">
      <h2 class="heading heading--light">What does Greenway Outdoor Support Services do?<span class="heading-rule"></span></h2>
      <p class="copy copy--light">We support participants to feel at home in the outdoors through small group and one-on-one activities in local bushland.</p>
    </div>
    <ul class="benefits">
      <li class="benefit">
        <svg class="benefit__icon" viewBox="0 0 40 40"><circle cx="20" cy="20" r="19" fill="#36a234"/><path d="M12 20 l6 6 l11-12" stroke="#fff" stroke-width="3.5" fill="none" stroke-linecap="round" stroke-linejoin="round"/></svg>
        <div><p class="benefit__title">Accessible</p><p class="benefit__text">Supports are local, safe, and transport can be arranged.</p></div>
      </li>
      <li class="benefit">
        <svg class="benefit__icon" viewBox="0 0 40 40"><circle cx="20" cy="20" r="19" fill="#36a234"/><circle cx="14" cy="16" r="2.2" fill="#fff"/><circle cx="26" cy="16" r="2.2" fill="#fff"/><path d="M12 23 q8 8 16 0" stroke="#fff" stroke-width="3" fill="none" stroke-linecap="round"/></svg>
        <div><p class="benefit__title">Enjoyable</p><p class="benefit__text">Activities are engaging, relaxed and non-stigmatising.</p></div>
      </li>
      <li class="benefit">
        <svg class="benefit__icon" viewBox="0 0 40 40"><circle cx="20" cy="20" r="19" fill="#36a234"/><path d="M20 30 C8 22 10 12 16 12 C18 12 20 14 20 16 C20 14 22 12 24 12 C30 12 32 22 20 30 Z" fill="#fff"/></svg>
        <div><p class="benefit__title">Beneficial</p><p class="benefit__text">Participants access the wellbeing benefits of nature while gaining knowledge, skills and experiences.</p></div>
      </li>
    </ul>
  </div>

  <div class="panel panel--middle">
    <div class="what-is">
      <h2 class="heading heading--green">What is <span class="accent">'Nature-Connection'</span>?</h2>
      <p class="copy copy--dark">Humans have always lived as part of nature. Feeling connected to the natural world supports our health and sense of belonging.</p>
      <ul class="ticks">
        <li>Lower stress and anxiety</li>
        <li>Improved mood and focus</li>
        <li>Greater confidence</li>
        <li>Social connection</li>
        <li>Care for the environment</li>
      </ul>
      <p class="copy copy--dark">Unfortunately, many of us now spend little time outdoors. Our programs offer a gentle way back.</p>
    </div>
  </div>

  <div class="panel panel--right">
    <div class="doing">
      <h2 class="heading heading--green">What will <span class="accent">I be doing?</span></h2>
      <p class="copy copy--dark">Together we will go bushwalking, camping and practise bushcraft skills such as fire lighting, shelter building and plant identification. Activities are shaped around your goals and pace.</p>
    </div>
    <div class="where">
      <h2 class="heading heading--green">Where will <span class="accent">I be doing?</span></h2>
      <p class="copy copy--dark">Sessions take place in parks, reserves and bushland close to home, with longer trips to national parks as confidence grows.</p>
    </div>
  </div>
</section>

</body>
</html>
```